Web App UI Design prototype

I have a sketch of a series of pages for a new web app, and would like to develop a clean, user friendly, intuitive design around the content.

Target Market(s)

small to medium sized business owners

Number of Pages Required

5+ page

Font styles to use
Sans Serif

Colors
33a6d7
85cae6
33b8a4
86cfc6
886aae
faa54b
000000
757575
cbcbcb

Requirements
Must have
• Color pallet that fits with my logo
• Clean modern, timeless design
• Intuitive use of UI
• Icons always help

```html
<!DOCTYPE html>
<html lang="en">
<head>
<meta charset="utf-8">
<title>Vireo Dashboard</title>
<link rel="stylesheet" href="https://fonts.googleapis.com/css2?family=Open+Sans:wght@400;600;700&display=swap">
<style>
:root{
  --canvas:#e1e1e1;
  --sidebar:#0f1b3a;
  --sidebar-text:#a9b3c9;
  --white:#ffffff;
  --ink:#1f2a44;
  --muted:#6b7280;
  --line:#e6e6e6;
  --blue:#4a7de0;
  --navy:#2c3a5c;
  --teal:#43cea2;
  --sky:#4aa9e0;
  --grey:#d9d9d9;
  --red:#e8452c;
  --green:#23a55a;
  --brand:#33a6d7;
  --accent:#33b8a4;
}
*{box-sizing:border-box;margin:0;padding:0}
html,body{width:1200px;height:668px;overflow:hidden;background:var(--canvas);font-family:"Open Sans",sans-serif;color:var(--ink)}
.app{position:relative;width:1200px;height:668px}
.sidebar{position:absolute;left:0;top:0;width:195px;height:668px;background:var(--sidebar);color:var(--white)}
.brand{position:absolute;left:36px;top:30px;display:flex;align-items:center;gap:10px;font-size:25px;font-weight:400;color:var(--brand)}
.brand-dot{width:18px;height:18px;border-radius:50%;background:var(--brand)}
.nav-group{position:absolute;left:28px;width:150px}
.nav-head{display:flex;align-items:center;gap:8px;font-size:11px;font-weight:600;height:20px}
.nav-head .caret{margin-left:auto;border:4px solid transparent;border-top-color:var(--sidebar-text);border-bottom:0}
.nav-item{font-size:11px;color:var(--sidebar-text);padding-left:28px;height:35px;line-height:35px}
.topbar{position:absolute;left:195px;top:0;width:1005px;height:61px;background:var(--white);border-bottom:1px solid #d6d6d6}
.menu-icon{position:absolute;left:16px;top:21px}
.company{position:absolute;left:56px;top:18px;font-size:18px;font-weight:700;letter-spacing:.5px;color:#3b3f4a}
.search{position:absolute;left:439px;top:16px;width:128px;height:30px;border-radius:15px;background:#f1f1f1;border:1px solid #e3e3e3}
.search svg{position:absolute;right:8px;top:7px}
.top-link{position:absolute;top:21px;font-size:13px;display:flex;align-items:center;gap:6px;color:#3b3f4a;white-space:nowrap}
.top-link.active{color:var(--brand)}
.active-bar{position:absolute;left:679px;top:58px;width:90px;height:3px;background:var(--brand)}
.badge{width:14px;height:14px;border-radius:50%;background:var(--accent);color:var(--white);font-size:9px;font-weight:700;display:inline-flex;align-items:center;justify-content:center}
.divider{position:absolute;top:20px;width:1px;height:20px;background:#d6d6d6}
.avatar{position:absolute;left:931px;top:9px;width:38px;height:38px;border-radius:50%;background:radial-gradient(circle at 50% 40%,#c99a7a,#5a3a2a)}
.page-title{position:absolute;left:219px;top:78px;font-size:20px;font-weight:400;display:flex;align-items:center;gap:8px}
.filters{position:absolute;top:75px;left:774px;display:flex;gap:6px}
.filter{height:31px;padding:0 12px;border-radius:16px;border:1px solid #c8c8c8;background:#ececec;font-size:13px;color:#444;display:flex;align-items:center;gap:4px}
.card{position:absolute;background:var(--white)}
.card-title{position:absolute;left:24px;top:16px;font-size:18px;font-weight:400;color:var(--ink)}
.sales{left:211px;top:124px;width:380px;height:252px}
.range{position:absolute;right:30px;top:22px;font-size:12px;font-weight:600}
.range::after{content:"";display:inline-block;margin-left:7px;border:3.5px solid transparent;border-top-color:var(--ink);vertical-align:middle}
.chart{position:absolute;left:16px;top:52px}
.sales-foot{position:absolute;left:24px;top:196px;font-size:18px}
.sales-foot small{display:block;font-size:8px;font-weight:600;color:#555;margin-top:-3px}
.finance-top{left:610px;top:124px;width:379px;height:252px}
.figures{position:absolute;left:30px;top:56px;display:flex;align-items:flex-start}
.figure .num{font-size:28px;line-height:32px}
.figure .cur{font-size:12px;margin-left:4px}
.figure .label{font-size:15px;font-weight:600;margin-top:-2px}
.expense .num,.expense .cur{color:var(--red)}
.income .num,.income .cur{color:var(--green)}
.dash{width:14px;height:3px;background:var(--navy);margin:22px 10px 0}
.stack{position:absolute;left:22px;top:154px;width:310px;height:6px;border-radius:3px;overflow:hidden;display:flex;background:var(--grey)}
.legend-small{position:absolute;left:22px;top:176px;width:330px;display:grid;grid-template-columns:112px 103px 100px;row-gap:14px;font-size:9px;color:#444}
.legend-small span::before{content:"";display:inline-block;width:6px;height:6px;border-radius:50%;background:var(--c);margin-right:4px}
.documents{left:1005px;top:124px;width:182px;height:252px}
.documents .card-title{left:16px}
.doc{position:absolute;left:0;width:182px;height:67px;border-bottom:1px solid var(--line)}
.doc svg{position:absolute;left:18px;top:16px}
.doc-name{position:absolute;left:49px;top:15px;font-size:12px;font-weight:600}
.doc-size{position:absolute;left:49px;top:33px;font-size:8px;color:#555}
.scroll{position:absolute;right:6px;top:70px;width:3px;height:34px;background:#ccc;border-radius:2px}
.finance-bottom{left:211px;top:392px;width:380px;height:251px}
.count{position:absolute;right:24px;top:20px;width:21px;height:21px;border-radius:50%;background:var(--navy);color:var(--white);font-size:12px;display:flex;align-items:center;justify-content:center}
.donut{position:absolute;left:30px;top:72px}
.legend{position:absolute;left:206px;top:68px;list-style:none;font-size:13px}
.legend li{height:27px;display:flex;align-items:center;gap:8px}
.legend li::before{content:"";width:10px;height:10px;border-radius:50%;background:var(--c)}
.actions{position:absolute;left:26px;top:209px;display:flex;gap:40px;font-size:13px;font-weight:700}
</style>
</head>
<body>
<div class="app">
  <aside class="sidebar">
    <div class="brand"><span class="brand-dot"></span>Vireo</div>
    <div class="nav-group" style="top:110px">
      <div class="nav-head">
        <svg width="20" height="12" viewBox="0 0 20 12"><circle cx="10" cy="3" r="3" fill="#fff"/><circle cx="4" cy="4" r="2.2" fill="#fff"/><circle cx="16" cy="4" r="2.2" fill="#fff"/><path d="M5 12a5 5 0 0 1 10 0z" fill="#fff"/><path d="M0 12a4 4 0 0 1 6-3.5L5 12zM20 12a4 4 0 0 0-6-3.5L15 12z" fill="#fff"/></svg>
        Departments<span class="caret"></span>
      </div>
      <div style="margin-top:8px">
        <div class="nav-item">Sales&amp;Marketing</div>
        <div class="nav-item">Operations</div>
        <div class="nav-item">Finance</div>
        <div class="nav-item">Admin</div>
      </div>
    </div>
    <div class="nav-group" style="top:313px">
      <div class="nav-head">
        <svg width="20" height="14" viewBox="0 0 20 14"><rect x="3" y="0" width="14" height="2.5" fill="#fff"/><rect x="3" y="5.5" width="14" height="2.5" fill="#fff"/><rect x="3" y="11" width="14" height="2.5" fill="#fff"/></svg>
        Process<span class="caret"></span>
      </div>
      <div style="margin-top:8px">
        <div class="nav-item">All</div>
        <div class="nav-item">Saved</div>
        <div class="nav-item">Recent</div>
      </div>
    </div>
  </aside>

  <header class="topbar">
    <svg class="menu-icon" width="18" height="14" viewBox="0 0 18 14"><rect width="18" height="2.5" fill="#bbb"/><rect y="5.5" width="18" height="2.5" fill="#bbb"/><rect y="11" width="18" height="2.5" fill="#bbb"/></svg>
    <div class="company">NORVA</div>
    <div class="search"><svg width="14" height="14" viewBox="0 0 14 14"><circle cx="6" cy="6" r="4.5" stroke="#aaa" stroke-width="1.5" fill="none"/><path d="M9.5 9.5L13 13" stroke="#aaa" stroke-width="1.5"/></svg></div>
    <div class="top-link" style="left:601px"><svg width="13" height="12" viewBox="0 0 13 12"><path d="M6.5 0L13 6h-2v6H8V8H5v4H2V6H0z" fill="#aaa"/></svg>Home</div>
    <div class="top-link active" style="left:679px"><svg width="15" height="12" viewBox="0 0 15 12"><path d="M7.5 0A7.5 7.5 0 0 0 0 7.5V12h15V7.5A7.5 7.5 0 0 0 7.5 0z" fill="#33a6d7"/><path d="M7.5 9L10.5 4" stroke="#fff" stroke-width="1.6"/><circle cx="7.5" cy="9" r="1.4" fill="#fff"/></svg>Dashboard</div>
    <div class="active-bar"></div>
    <div class="divider" style="left:784px"></div>
    <div class="top-link" style="left:794px;font-size:11px;font-weight:600"><span class="badge">2</span>Updates<svg width="8" height="5" viewBox="0 0 8 5"><path d="M0 0h8L4 5z" fill="#333"/></svg></div>
    <div class="divider" style="left:885px"></div>
    <svg style="position:absolute;left:895px;top:23px" width="15" height="15" viewBox="0 0 15 15"><path d="M12.5 7.5A5 5 0 1 1 9.5 3" stroke="#555" stroke-width="1.8" fill="none"/><path d="M8 0l4 3-4 3z" fill="#555"/></svg>
    <div class="divider" style="left:917px"></div>
    <div class="avatar" role="img" aria-label="User profile photo"></div>
  </header>

  <h1 class="page-title">
    <svg width="20" height="17" viewBox="0 0 15 12"><path d="M7.5 0A7.5 7.5 0 0 0 0 7.5V12h15V7.5A7.5 7.5 0 0 0 7.5 0z" fill="#33b8a4"/><path d="M7.5 9L10.5 4" stroke="#fff" stroke-width="1.6"/><circle cx="7.5" cy="9" r="1.4" fill="#fff"/></svg>
    Dashboard
  </h1>
  <div class="filters">
    <div class="filter">Depratment<svg width="9" height="6" viewBox="0 0 9 6"><path d="M1 1l3.5 3.5L8 1" stroke="#555" fill="none"/></svg></div>
    <div class="filter">Statuses<svg width="9" height="6" viewBox="0 0 9 6"><path d="M1 1l3.5 3.5L8 1" stroke="#555" fill="none"/></svg></div>
    <div class="filter">Assignment<svg width="9" height="6" viewBox="0 0 9 6"><path d="M1 1l3.5 3.5L8 1" stroke="#555" fill="none"/></svg></div>
    <div class="filter">Date<svg width="9" height="6" viewBox="0 0 9 6"><path d="M1 1l3.5 3.5L8 1" stroke="#555" fill="none"/></svg></div>
  </div>

  <section class="card sales">
    <h2 class="card-title">Sales</h2>
    <div class="range">Jan-Sep</div>
    <svg class="chart" width="345" height="136" viewBox="0 0 345 136" font-family="Open Sans, sans-serif" font-size="7" fill="#333">
      <text x="2" y="9">30</text><text x="2" y="45">20</text><text x="2" y="81">10</text><text x="2" y="118">01</text>
      <line x1="20" y1="6" x2="20" y2="118" stroke="#ddd"/>
      <g stroke="#ccc" stroke-dasharray="1 2">
        <line x1="58" y1="6" x2="58" y2="118"/><line x1="97" y1="6" x2="97" y2="118"/><line x1="134" y1="6" x2="134" y2="118"/><line x1="172" y1="6" x2="172" y2="118"/><line x1="210" y1="6" x2="210" y2="118"/><line x1="250" y1="6" x2="250" y2="118"/><line x1="288" y1="6" x2="288" y2="118"/>
      </g>
      <g fill="#222"><circle cx="58" cy="6" r="1.3"/><circle cx="97" cy="6" r="1.3"/><circle cx="134" cy="6" r="1.3"/><circle cx="172" cy="6" r="1.3"/><circle cx="210" cy="6" r="1.3"/><circle cx="250" cy="6" r="1.3"/><circle cx="288" cy="6" r="1.3"/></g>
      <path d="M20 118C40 70 60 40 95 44C130 48 125 95 160 90C200 85 200 20 250 24C300 28 300 90 315 95C325 98 330 80 332 70L332 118Z" fill="#86e0c4" fill-opacity=".6"/>
      <path d="M20 118C30 80 45 56 60 54C80 52 80 80 92 52C100 36 110 50 120 62C140 84 160 90 190 56C215 30 240 36 260 60C285 95 300 98 332 95L332 118Z" fill="#7a8ee0" fill-opacity=".45"/>
      <path d="M20 118C40 80 60 50 90 50C120 50 135 90 160 90C195 90 205 35 235 36C270 37 275 96 310 97C325 98 330 85 332 75L332 118Z" fill="#6fa6d8" fill-opacity=".7"/>
      <g font-size="7"><text x="18" y="130">Jan</text><text x="52" y="130">Feb</text><text x="90" y="130">Mar</text><text x="128" y="130">Apr</text><text x="166" y="130">May</text><text x="202" y="130">June</text><text x="245" y="130">Jul</text><text x="281" y="130">Aug</text><text x="320" y="130">Sep</text></g>
    </svg>
    <div class="sales-foot">Sales<small>Available Nodes with their states</small></div>
  </section>

  <section class="card finance-top">
    <h2 class="card-title">Finance</h2>
    <div class="figures">
      <div class="figure expense"><div><span class="num">25258</span><span class="cur">USD</span></div><div class="label">Expense</div></div>
      <div class="dash"></div>
      <div class="figure income"><div><span class="num">455823</span><span class="cur">USD</span></div><div class="label">Income</div></div>
    </div>
    <div class="stack">
      <i style="width:40px;background:var(--blue)"></i><i style="width:61px;background:var(--navy)"></i><i style="width:76px;background:var(--blue)"></i><i style="width:64px;background:var(--teal)"></i>
    </div>
    <div class="legend-small">
      <span style="--c:var(--blue)">Marketing</span><span style="--c:var(--blue)">Administration</span><span style="--c:var(--grey)">Others</span>
      <span style="--c:var(--navy)">Office Expenses</span><span style="--c:var(--teal)">Salary</span>
    </div>
  </section>

  <section class="card documents">
    <h2 class="card-title">Documents</h2>
    <div class="doc" style="top:51px"><svg width="22" height="32" viewBox="0 0 22 32"><path d="M0 0h15l7 7v25H0z" fill="#e2e2e2"/><path d="M11 12v13M6 20l5 5 5-5" stroke="#fff" stroke-width="1.5" fill="none"/></svg><div class="doc-name">Sales Contract</div><div class="doc-size">120 Kb</div></div>
    <div class="doc" style="top:118px"><svg width="22" height="32" viewBox="0 0 22 32"><path d="M0 0h15l7 7v25H0z" fill="#e2e2e2"/><path d="M11 12v13M6 20l5 5 5-5" stroke="#fff" stroke-width="1.5" fill="none"/></svg><div class="doc-name">Lease Agreement</div><div class="doc-size">332 Kb</div></div>
    <div class="doc" style="top:185px;border:0"><svg width="22" height="32" viewBox="0 0 22 32"><path d="M0 0h15l7 7v25H0z" fill="#e2e2e2"/><path d="M11 12v13M6 20l5 5 5-5" stroke="#fff" stroke-width="1.5" fill="none"/></svg><div class="doc-name">Attroney Review</div><div class="doc-size">520 Kb</div></div>
    <div class="scroll"></div>
  </section>

  <section class="card finance-bottom">
    <h2 class="card-title">Finance</h2>
    <div class="count">2</div>
    <svg class="donut" width="116" height="116" viewBox="0 0 116 116" font-family="Open Sans, sans-serif">
      <g transform="rotate(200 58 58)" fill="none" stroke-width="15">
        <circle cx="58" cy="58" r="49" stroke="#4a7de0" stroke-dasharray="132 308"/>
        <circle cx="58" cy="58" r="49" stroke="#43cea2" stroke-dasharray="47 308" stroke-dashoffset="-132"/>
        <circle cx="58" cy="58" r="49" stroke="#d9d9d9" stroke-dasharray="38 308" stroke-dashoffset="-179"/>
        <circle cx="58" cy="58" r="49" stroke="#4aa9e0" stroke-dasharray="60 308" stroke-dashoffset="-217"/>
        <circle cx="58" cy="58" r="49" stroke="#2c3a5c" stroke-dasharray="31 308" stroke-dashoffset="-277"/>
      </g>
      <text x="58" y="55" text-anchor="middle" font-size="9" fill="#222">Total</text>
      <text x="58" y="70" text-anchor="middle" font-size="14" fill="#222">$45585</text>
    </svg>
    <ul class="legend">
      <li style="--c:var(--blue)">Marketing</li>
      <li style="--c:var(--teal)">Administration</li>
      <li style="--c:var(--sky)">Salary</li>
      <li style="--c:var(--navy)">office expenses</li>
      <li style="--c:var(--grey)">Others</li>
    </ul>
    <div class="actions"><span>Add new</span><span>Edit Contact</span></div>
  </section>
</div>
</body>
</html>
```